Agency needs 2 x EDM executions

We’re Brindle, a word of mouth marketing agency. We have a community of people who participate in projects that range from being sent free products to trying new services to road test. Pretty fun stuff!

We’re looking for a designer to create two EDM (electronic direct marketing) executions. These EDMs will be used as an email to get people to join and become a Brindle member.

Previous examples of our EDMs are attached, but we’re looking for some fresh new design ideas! Look & feel to be fun, playful, easy on the eye. Most of all they need to be attention grabbing and motivating enough for the readers to click through and join (rather than scanning and deleting the email!).

The two executions we require will differ slightly in content and design. Copy that needs to be included in each of the EDMs is attached.

Specifically, version 1:
• Needs to include two event photos with their description below, similar to Clipwall (refer to copy document as a guide)
• Include a collage of recent product images (again, can see a guide in the copy document). Due to space restrictions you may only be able to fit one or two lines of a collage.
• Down the bottom is a quote from a member, we would like to see this stand out from the rest of the text.

And version 2:
• This will also have a collage of recent product images, but because this version has more space you can fit more images.
• This time there are two quotes from two different members.

The EDMs need to be:
• 550 pixels wide and 1000 pixels in height.
• JPEG

Please visit our website to get an idea of our branding: www.thebrindle.com.au

Requirements
Must have
• Both designs need to include:

• Copy which is found in the attached document
• Brindle logo
• ‘Join now’ button (call to action)
• Website URL: thebrindle.com.au
• Century gothic font and luna font.
Nice to have
• Whilst the background doesn’t need to be all yellow, and can be white, we’d like to have at least some yellow per branding. The yellow we use is 100% yellow.

```html
<!DOCTYPE html>
<html lang="en">
<head>
<meta charset="utf-8">
<title>Join Brindle</title>
<link rel="stylesheet" href="https://fonts.googleapis.com/css2?family=Mulish:wght@400;700;800&family=Gochi+Hand&display=swap">
<style>
  :root {
    --yellow: #fff200;
    --yellow-pale: #fffbc2;
    --black: #111111;
    --ink: #1c1c1c;
    --grey: #555555;
    --white: #ffffff;
    --page: #f4f4f4;
  }
  * { box-sizing: border-box; margin: 0; padding: 0; }
  html, body { width: 1200px; height: 2400px; overflow: hidden; background: var(--page); }

  /* 550 x 1000 email, drawn at 1200 x 2182 */
  .edm {
    position: relative;
    width: 1200px;
    height: 2182px;
    overflow: hidden;
    background: var(--white);
    font-family: "Mulish", "Century Gothic", sans-serif;
    color: var(--ink);
  }

  .top-bar {
    position: absolute; left: 0; top: 0; width: 1200px; height: 120px;
    background: var(--black);
    display: flex; align-items: center; justify-content: space-between;
    padding: 0 60px;
  }
  .brand {
    display: flex; align-items: center; gap: 14px;
    font-weight: 800; font-size: 54px; color: var(--yellow);
  }
  .brand-dot { width: 28px; height: 28px; border-radius: 50%; background: var(--yellow); }
  .top-site { font-weight: 700; font-size: 32px; color: var(--white); }

  .hero {
    position: absolute; left: 0; top: 120px; width: 1200px; height: 540px;
    background: var(--yellow);
  }
  .hero-bubble { position: absolute; left: 0; top: 0; }
  .hero-title {
    position: absolute; left: 120px; top: 70px; width: 960px;
    text-align: center; font-family: "Gochi Hand", cursive; color: var(--black);
  }
  .hero-title h1 { font-size: 124px; font-weight: 400; line-height: 136px; }
  .hero-title p { font-size: 48px; line-height: 60px; margin-top: 14px; }

  .events {
    position: absolute; left: 60px; top: 690px; width: 1080px;
    display: flex; justify-content: space-between;
  }
  .event { width: 520px; }
  .event-photo {
    width: 520px; height: 300px; border-radius: 24px;
    border: 8px solid var(--black);
  }
  .event-photo--launch { background: radial-gradient(circle at 50% 60%, #eadfce 0, #c9a27e 55%, #6d5a48 100%); }
  .event-photo--kitchen { background: radial-gradient(circle at 50% 55%, #d8c2a8 0, #8a97a3 60%, #3e4046 100%); }
  .event-caption {
    margin-top: 18px; font-size: 30px; line-height: 42px; color: var(--grey);
  }

  .how {
    position: absolute; left: 60px; top: 1150px; width: 1080px;
  }
  .how h2 { font-weight: 800; font-size: 56px; line-height: 70px; color: var(--black); }
  .how-mark { display: inline-block; width: 22px; height: 22px; border-radius: 50%; background: var(--yellow); border: 5px solid var(--black); margin-right: 14px; vertical-align: 6px; }
  .how p { margin-top: 18px; font-size: 34px; line-height: 50px; }
  .how strong { font-weight: 800; background: var(--yellow); padding: 0 6px; }

  .products-title {
    position: absolute; left: 60px; top: 1530px; width: 1080px;
    font-weight: 800; font-size: 32px; line-height: 40px;
  }
  .products {
    position: absolute; left: 60px; top: 1590px; width: 1080px; height: 180px;
    display: flex; justify-content: space-between;
  }
  .product {
    width: 200px; height: 180px; border-radius: 20px;
    border: 6px solid var(--yellow);
  }
  .product--stock { background: linear-gradient(180deg, #f6e04a, #e0a51c); }
  .product--haircare { background: linear-gradient(180deg, #f1ece4, #c98a4a); }
  .product--coconut { background: linear-gradient(180deg, #9bd45a, #3f8f3a); }
  .product--yoghurt { background: linear-gradient(180deg, #3a5ea8, #c64a5a); }
  .product--grater { background: linear-gradient(180deg, #f2f2f2, #c8262c); }

  .quote-card {
    position: absolute; left: 60px; top: 1810px; width: 1080px; height: 240px;
    background: var(--black); border-radius: 28px;
    padding: 30px 48px;
  }
  .quote {
    font-size: 34px; line-height: 46px; color: var(--white);
  }
  .quote-name {
    position: absolute; right: 48px; bottom: 18px;
    font-family: "Gochi Hand", cursive; font-size: 52px; line-height: 60px; color: var(--yellow);
  }

  .join-now {
    position: absolute; left: 390px; top: 2076px; width: 420px; height: 86px;
    border-radius: 43px; background: var(--yellow); border: 6px solid var(--black);
    display: flex; align-items: center; justify-content: center;
    font-weight: 800; font-size: 40px; color: var(--black); text-decoration: none;
  }
</style>
</head>
<body>
<main class="edm">
  <header class="top-bar">
    <p class="brand">Brindle<span class="brand-dot"></span></p>
    <p class="top-site">thebrindle.com.au</p>
  </header>

  <section class="hero">
    <svg class="hero-bubble" width="1200" height="540" viewBox="0 0 1200 540" aria-hidden="true">
      <path d="M250 400 L150 520 L380 440 Z" fill="#ffffff" stroke="#111111" stroke-width="10" stroke-linejoin="round"/>
      <ellipse cx="600" cy="250" rx="530" ry="215" fill="#ffffff" stroke="#111111" stroke-width="10"/>
      <path d="M262 395 L380 438" stroke="#ffffff" stroke-width="14"/>
    </svg>
    <div class="hero-title">
      <h1>Join Brindle</h1>
      <p>and trial the latest products in exchange<br>for your opinion and sharing with friends!</p>
    </div>
  </section>

  <section class="events">
    <figure class="event">
      <div class="event-photo event-photo--launch" role="img" aria-label="Photo of members celebrating at a Brindle launch night"></div>
      <figcaption class="event-caption">Members toast a new sparkling drink at our Sydney launch night.</figcaption>
    </figure>
    <figure class="event">
      <div class="event-photo event-photo--kitchen" role="img" aria-label="Photo of members trying a kitchen gadget together"></div>
      <figcaption class="event-caption">Friends whip up dinner with a trial kitchen gadget in Brisbane.</figcaption>
    </figure>
  </section>

  <section class="how">
    <h2><span class="how-mark"></span>It works like this:</h2>
    <p>Answer a few simple questions about yourself. You’ll then be invited to participate in projects which include being sent products to try and samples to share around. After that we’ll ask for your honest opinion (good or bad). <strong>It’s free to join and participate!</strong></p>
  </section>

  <h3 class="products-title">Products Brindle members recently trialled include:</h3>
  <div class="products">
    <div class="product product--stock" role="img" aria-label="Stock cubes and recipe base pouch"></div>
    <div class="product product--haircare" role="img" aria-label="Hair care bottles"></div>
    <div class="product product--coconut" role="img" aria-label="Coconut water carton"></div>
    <div class="product product--yoghurt" role="img" aria-label="Yoghurt tub"></div>
    <div class="product product--grater" role="img" aria-label="Electric slicer and grater"></div>
  </div>

  <section class="quote-card">
    <blockquote class="quote">“It was such a fun project. I had a great time sharing it around and loved being the one to introduce such a great product to my friends!”</blockquote>
    <p class="quote-name">Megan, NSW</p>
  </section>

  <a class="join-now" href="https://www.thebrindle.com.au">Join now</a>
</main>
</body>
</html>
```